Packing Design: SNACK FOOD BAG

We are manufactures and our main product is a kind of shell-shaped corn puff in ketchup flavor: brand name is Zebrin. (See photo Red Zebrin Flips Ketchup)

We will launch 15 new products (like chips, tortilla, popcorn, biscuits, etc.) under the same logo Zebrin.
As new Products are different, their layout must be different or with different designs.
But they must all be connected together with any feature, to be easily recognized / identified as same Zebrin range of products.
-

THE MAIN PURPOSE OF THIS PROJECT CONTEST IS:

Choosing the best connection between “Red Zebrin flips ketchup" label and new designs for new products.
Customers must easily understand that new products are done from same Zebrin Factory and are part of the same Zebrin brand (production). We want new labels to naturally derive from old Zebrin design with a modern and hip connection.

We would prefer drafts where 1 part is in red color (including Zebrin Logo) and the rest of layout to be used for different designs (for different products). At the end of all different designs, they may have in common a part of their layouts, derived from Red Zebrin Ketchup.
But we warmly welcome your different ideas and different suggestions.

-
Send sample draft for any from products below:
PEANUT BUTTER CORN bag size: High 210 mm x Width 145 mm
TORTILLA CHIPS ( flavors: Nachos / Spicy Ketchup) bag size: High 160 mm x Width 130 mm
CRUNCHY CROUTONS bag size: High 160 mm x Width 115 mm
CARAMEL CORN bag size: High 210 mm x Width 145 mm

Bags are (no transparent) BOPP material, with different sizes, containing small quantities from 20 – 50 grams.
-
Details for this project can be downloaded clicking to the link below:
http://www.filevault-example.net/file/4r8k21 and
http://www.filevault-example.net/file/w73m5q

Reason: there are designers submitting designs at the last moments. there is no time to review and give feedback to all. apologies for any inconvenience caused to the designers who submitted earlier warm regards

Target Market(s)

Target customers are young people: children, teens, students.

Industry/Entity Type

Factory

Requirements
Must have
• The new designs must include SAME Zebrin Logo, few pieces of the product view with flavor images and FEATURES CONNECTING ALL DESIGNS TOGETHER.
Nice to have
• A Feature is needed, to connect all new products with "Zebrin flips ketchup" design and all designs together.
Connections could be any details like:
RED COLORED ribbons, RED COLORED dotted /spotted layout,
RED COLORED background containing lines within itself,
different nuances of Zebrin Logo,
or else, or else, etc.
Show us what inspires you...

We would like to see strong deep colors, with 3D or fading reflections within them.
Final designs should bring the sense of appetite (making your mouth wet).
Should not have
• - Zebrin-Logo must be used without the word 'Flips"
- Must no have connection with ZEBRIN carton character.
- we don't like that all products to be in all-in-red bags.

```html
<!DOCTYPE html>
<html lang="en">
<head>
<meta charset="utf-8">
<title>Zebrin Snack Bags</title>
<link href="https://fonts.googleapis.com/css2?family=Cabin+Sketch:wght@700&family=Architects+Daughter&display=swap" rel="stylesheet">
<style>
  :root {
    --canvas: #e6e6e7;
    --brand-red: #c4001b;
    --brand-red-deep: #a90016;
    --chalk: #ffffff;
    --ink: #111111;
    --note: #6b4a2a;

    --tortilla-side: #f5ae45;
    --tortilla-mid: #fbd596;
    --tortilla-light: #fde2b4;
    --tortilla-band: #bd0016;
    --tortilla-photo-a: #f2c343;
    --tortilla-photo-b: #d99a1f;

    --crouton-side: #ad6a48;
    --crouton-mid: #dba98a;
    --crouton-light: #ecc6ad;
    --crouton-band: #1c5a2c;
    --crouton-band-edge: #123f1d;
    --crouton-photo-a: #e7a458;
    --crouton-photo-b: #b8642c;
  }
  * { box-sizing: border-box; margin: 0; padding: 0; }
  html, body { width: 1200px; height: 900px; overflow: hidden; }
  body { background: var(--canvas); position: relative; font-family: "Cabin Sketch", cursive; }

  .bag {
    position: absolute; top: 125px; width: 410px; height: 595px; overflow: hidden;
    background: linear-gradient(90deg, var(--side) 0 83px, var(--mid) 83px 327px, var(--side) 327px 100%);
  }
  .bag::before {
    content: ""; position: absolute; left: 83px; right: 84px; top: 0; bottom: 0;
    background: linear-gradient(180deg, var(--mid) 0%, var(--light) 70%, var(--mid) 100%);
  }
  .bag--tortilla { left: 157px; --side: var(--tortilla-side); --mid: var(--tortilla-mid); --light: var(--tortilla-light); --band: var(--tortilla-band); --trim: var(--brand-red); }
  .bag--crouton { left: 632px; --side: var(--crouton-side); --mid: var(--crouton-mid); --light: var(--crouton-light); --band: var(--crouton-band); --trim: var(--crouton-band-edge); }

  .top-strip { position: absolute; left: 0; top: 0; width: 100%; height: 18px; background: var(--brand-red); }
  .bottom-strip { position: absolute; left: 0; bottom: 0; width: 100%; height: 15px; background: var(--trim); }

  .brand-panel { position: absolute; left: 83px; top: 18px; width: 243px; height: 254px; }
  .brand-panel svg { display: block; }
  .brand-name {
    position: absolute; left: 0; top: 138px; width: 100%; text-align: center;
    font-family: "Cabin Sketch", cursive; font-weight: 700; font-size: 64px; color: var(--chalk);
  }

  .open-note {
    position: absolute; left: 18px; top: 74px; width: 50px; text-align: center;
    font-family: "Architects Daughter", cursive; font-size: 12px; line-height: 1.25; color: var(--note); opacity: .8;
  }
  .open-arrow { position: absolute; left: 22px; top: 20px; }

  .title-band {
    position: absolute; left: 0; top: 345px; width: 100%; height: 115px; background: var(--band);
    clip-path: polygon(0 4%, 20% 0, 45% 5%, 70% 1%, 100% 4%, 100% 96%, 75% 100%, 50% 95%, 25% 100%, 0 96%);
    text-align: center; color: var(--chalk); font-family: "Cabin Sketch", cursive; font-weight: 700;
  }
  .bag--tortilla .title-line--main { font-size: 42px; letter-spacing: 2px; margin-top: 10px; line-height: 1; }
  .bag--tortilla .title-line--sub { font-size: 28px; letter-spacing: 2px; line-height: 1; }
  .bag--crouton .title-line--sub { font-size: 30px; letter-spacing: 2px; margin-top: 12px; line-height: 1; }
  .bag--crouton .title-line--main { font-size: 42px; letter-spacing: 2px; line-height: 1; }

  .product-photo { position: absolute; border-radius: 40% 45% 35% 40%; }
  .bag--tortilla .product-photo { left: 138px; top: 422px; width: 135px; height: 108px; background: radial-gradient(circle at 45% 40%, var(--tortilla-photo-a), var(--tortilla-photo-b)); }
  .bag--crouton .product-photo { left: 135px; top: 428px; width: 125px; height: 100px; background: radial-gradient(circle at 45% 40%, var(--crouton-photo-a), var(--crouton-photo-b)); }

  .flavor-note {
    position: absolute; font-family: "Architects Daughter", cursive; font-size: 13px; line-height: 1.2;
    color: var(--note); text-align: center; transform: rotate(58deg); opacity: .85;
  }
  .bag--tortilla .flavor-note { left: 278px; top: 478px; }
  .bag--crouton .flavor-note { left: 298px; top: 474px; }
  .flavor-arrow { position: absolute; left: 280px; top: 505px; }

  .weight-badge {
    position: absolute; left: 46px; top: 528px; width: 72px; height: 52px; border-radius: 50%;
    background: var(--ink); color: var(--chalk); display: flex; align-items: center; justify-content: center;
    font-family: "Architects Daughter", cursive; font-size: 17px;
  }
</style>
</head>
<body>

<svg width="0" height="0" style="position:absolute">
  <defs>
    <pattern id="zigzag" width="10" height="12" patternUnits="userSpaceOnUse">
      <polygon points="0,0 10,0 5,12" fill="#c4001b"/>
    </pattern>
  </defs>
</svg>

<article class="bag bag--tortilla">
  <div class="top-strip"></div>
  <svg class="open-arrow" width="30" height="50" viewBox="0 0 30 50" fill="none" stroke="#6b4a2a" stroke-width="1.2" opacity=".7">
    <path d="M12 48 C4 34 6 16 14 4"/><path d="M8 8 L14 3 L17 10"/>
  </svg>
  <p class="open-note">OPEN HERE</p>
  <div class="brand-panel">
    <svg width="243" height="254" viewBox="0 0 243 254">
      <rect width="243" height="242" fill="#c4001b"/>
      <rect y="242" width="243" height="12" fill="url(#zigzag)"/>
    </svg>
    <span class="brand-name">Zebrin</span>
  </div>
  <h2 class="title-band">
    <div class="title-line--main">TORTILLA</div>
    <div class="title-line--sub">CHIPS</div>
  </h2>
  <div class="product-photo" role="img" aria-label="Pile of cheese flavored tortilla chips"></div>
  <p class="flavor-note">CHEESE<br>FLAVORED</p>
  <svg class="flavor-arrow" width="50" height="40" viewBox="0 0 50 40" fill="none" stroke="#6b4a2a" stroke-width="1.2" opacity=".7">
    <path d="M40 2 C42 24 30 34 8 36"/><path d="M14 30 L7 36 L14 40"/>
  </svg>
  <div class="weight-badge">50gr.</div>
  <div class="bottom-strip"></div>
</article>

<article class="bag bag--crouton">
  <div class="top-strip"></div>
  <svg class="open-arrow" width="30" height="50" viewBox="0 0 30 50" fill="none" stroke="#6b4a2a" stroke-width="1.2" opacity=".7">
    <path d="M12 48 C4 34 6 16 14 4"/><path d="M8 8 L14 3 L17 10"/>
  </svg>
  <p class="open-note">OPEN HERE</p>
  <div class="brand-panel">
    <svg width="243" height="254" viewBox="0 0 243 254">
      <rect width="243" height="242" fill="#c4001b"/>
      <rect y="242" width="243" height="12" fill="url(#zigzag)"/>
    </svg>
    <span class="brand-name">Zebrin</span>
  </div>
  <h2 class="title-band">
    <div class="title-line--sub">CRUNCHY</div>
    <div class="title-line--main">CROUTONS</div>
  </h2>
  <div class="product-photo" role="img" aria-label="Handful of golden herb croutons with a basil leaf"></div>
  <p class="flavor-note">GREAT<br>TASTE</p>
  <svg class="flavor-arrow" width="50" height="40" viewBox="0 0 50 40" fill="none" stroke="#6b4a2a" stroke-width="1.2" opacity=".7">
    <path d="M40 2 C42 24 30 34 8 36"/><path d="M14 30 L7 36 L14 40"/>
  </svg>
  <div class="weight-badge">20gr.</div>
  <div class="bottom-strip"></div>
</article>

</body>
</html>
```